quorvaAgency Business Card Design Project

We need a business card design for quorvaAgency. quorvaAgency is an underwriting agency. Underwriting agencies act on behalf of insurers, to underwrite insurance. We will be operating in specialised classes of insurance initially and looking to expand from there. We would like to see designs that incorporate our logo colours as well as a contrasting stand out colour - also we'd like the logo itself to be embossed on the card.

Industry/Entity Type

Insurance

Requirements
Must have
• Logo on front
Nice to have
• Logo solely featured on back of card
Should not have
• Please do not use comic cans font :)

```html
<!DOCTYPE html>
<html lang="en">
<head>
<meta charset="utf-8">
<title>quorvaAgency Business Card</title>
<link rel="stylesheet" href="https://fonts.googleapis.com/css2?family=Open+Sans:wght@400;600;700&display=swap">
<style>
  :root {
    --page: #ffffff;
    --gold-light: #f1ede4;
    --gold-mid: #d6ccb9;
    --gold-deep: #bfb195;
    --brand-blue: #1d57a8;
    --ink-white: #ffffff;
    --panel: #ffffff;
  }
  * { margin: 0; padding: 0; box-sizing: border-box; }
  html, body {
    width: 1200px; height: 900px; overflow: hidden;
    background: var(--page);
    font-family: "Open Sans", Arial, sans-serif;
  }
  .canvas { position: relative; width: 1200px; height: 900px; }
  .card {
    position: absolute; left: 314px; width: 626px; height: 360px;
    border-radius: 22px; overflow: hidden;
    background: linear-gradient(110deg, var(--gold-light) 0%, var(--gold-mid) 45%, var(--gold-deep) 100%);
  }
  .card--front { top: 62px; }
  .card--back { top: 488px; }

  .wave-decoration {
    position: absolute; right: 0; bottom: 0; width: 320px; height: 120px;
    background: radial-gradient(ellipse at 70% 80%, rgba(255,255,255,0.75) 0%, rgba(255,255,255,0.25) 50%, rgba(255,255,255,0) 75%);
  }

  .brand {
    position: absolute; display: flex; flex-direction: column; align-items: center;
    transform: translateX(-50%);
  }
  .brand__dot {
    width: 72px; height: 72px; border-radius: 50%;
    background: var(--brand-blue); margin-bottom: 14px;
  }
  .brand__name {
    font-weight: 600; color: var(--brand-blue); letter-spacing: -1px; line-height: 1;
    white-space: nowrap;
  }
  .card--front .brand { left: 312px; top: 74px; }
  .card--front .brand__name { font-size: 56px; }

  .back-panel { position: absolute; left: 0; top: 0; }
  .card--back .brand { left: 188px; top: 92px; }
  .card--back .brand__dot { width: 64px; height: 64px; margin-bottom: 14px; }
  .card--back .brand__name { font-size: 44px; }

  .back-heading {
    position: absolute; right: 40px; top: 32px; text-align: right; color: var(--ink-white);
    white-space: nowrap;
  }
  .back-heading__name { font-size: 26px; font-weight: 600; line-height: 1.1; letter-spacing: -0.5px; }
  .back-heading__address { font-size: 16px; font-weight: 400; }

  .contact-list {
    position: absolute; left: 424px; top: 238px; list-style: none;
  }
  .contact-list li {
    display: flex; align-items: center; height: 30px;
    color: var(--ink-white); font-size: 12px; font-weight: 700; white-space: nowrap;
  }
  .contact-list svg { width: 18px; height: 18px; margin-right: 12px; flex: none; }
</style>
</head>
<body>
<div class="canvas">

  <section class="card card--front">
    <div class="wave-decoration" role="img" aria-label="Soft white flowing line pattern"></div>
    <div class="brand">
      <span class="brand__dot"></span>
      <span class="brand__name">quorvaAgency</span>
    </div>
  </section>

  <section class="card card--back">
    <svg class="back-panel" width="626" height="360" viewBox="0 0 626 360" aria-hidden="true">
      <path d="M22 18 H300 Q360 18 362 80 Q350 180 362 280 Q360 342 300 342 H22 Q14 342 14 334 V26 Q14 18 22 18 Z" fill="var(--panel)"/>
    </svg>
    <div class="brand">
      <span class="brand__dot"></span>
      <span class="brand__name">quorvaAgency</span>
    </div>

    <div class="back-heading">
      <div class="back-heading__name">quorvaAgency</div>
      <div class="back-heading__address">your address</div>
    </div>

    <ul class="contact-list">
      <li>
        <svg viewBox="0 0 18 18"><rect x="1" y="1" width="16" height="16" rx="3" fill="none" stroke="#fff" stroke-width="1.5"/><path d="M6 4 L8 6 L7 8 Q8 10 10 11 L12 10 L14 12 L12 14 Q6 13 4 6 Z" fill="#fff"/></svg>
        321-654-0987
      </li>
      <li>
        <svg viewBox="0 0 18 18"><rect x="2" y="4" width="14" height="10" fill="none" stroke="#fff" stroke-width="1.5"/><path d="M2 4 L9 10 L16 4" fill="none" stroke="#fff" stroke-width="1.5"/></svg>
        sales@quorvaAgency.com
      </li>
      <li>
        <svg viewBox="0 0 18 18"><rect x="2" y="2" width="14" height="14" rx="3" fill="none" stroke="#fff" stroke-width="1.5"/><rect x="5" y="6" width="8" height="6" fill="#fff"/></svg>
        www.quorvaAgency.com
      </li>
    </ul>
  </section>

</div>
</body>
</html>
```